2-page digital brochure highlighting company and service offerings to oil and gas market in W Canada

we are asked to send a quick info package to potential clients. Brief description of who Harrowfield Conduit Corp is and what we can offer our Oil & Gas, Midstream and engineering prospects. Our services include ; pipeline maintenance and integrity, abandonments and decommissioning, and project management. PP attached for pictures and verbiage. Branding guidelines below. want to promote services and safety

```html
<!DOCTYPE html>
<html lang="en">
<head>
<meta charset="utf-8">
<title>Harrowfield Conduit Corp – Info Brochure</title>
<link rel="stylesheet" href="https://fonts.googleapis.com/css2?family=Montserrat:wght@300;400;500;600;700;800&display=swap">
<style>
  :root {
    --stage: #9a4f1c;
    --teal-navy: #064b6d;
    --deep-navy: #043f5e;
    --night-navy: #0c2c4a;
    --orange: #e58a23;
    --white: #ffffff;
    --paper: #f1f1f1;
  }
  * { margin: 0; padding: 0; box-sizing: border-box; }
  html, body { width: 1035px; height: 1200px; overflow: hidden; }
  body {
    background: var(--stage);
    font-family: "Montserrat", sans-serif;
    display: flex;
    flex-direction: column;
    align-items: center;
    justify-content: space-evenly;
  }
  .page {
    width: 790px;
    height: 559px;
    display: block;
    box-shadow: 0 10px 24px rgba(0,0,0,0.35);
  }
  .page text { font-family: "Montserrat", sans-serif; }
  .wordmark { font-weight: 700; letter-spacing: 1px; }
  .headline-light { font-weight: 400; fill: var(--orange); }
  .headline-bold { font-weight: 800; fill: var(--white); }
  .tagline { font-weight: 500; fill: var(--white); }
  .url { font-weight: 600; fill: var(--white); letter-spacing: 3px; }
  .section-head { font-weight: 700; }
  .service-title { font-weight: 700; fill: var(--white); font-size: 12.5px; }
  .service-item { font-weight: 500; fill: var(--white); font-size: 8.6px; }
</style>
</head>
<body>

<!-- Page 1: cover -->
<svg class="page page-cover" viewBox="0 0 772 546" xmlns="http://www.w3.org/2000/svg">
  <defs>
    <linearGradient id="photoTone" x1="0" y1="0" x2="1" y2="1">
      <stop offset="0" stop-color="#2f5fb8"/>
      <stop offset="0.55" stop-color="#1d3f8e"/>
      <stop offset="1" stop-color="#d9b23a"/>
    </linearGradient>
  </defs>

  <rect class="cover-bg" width="772" height="546" fill="var(--teal-navy)"/>
  <polygon class="cover-bg-right" points="300,0 772,0 772,546 430,546" fill="var(--deep-navy)"/>

  <!-- white brand panel -->
  <polygon class="brand-panel" points="0,0 290,0 326,140 300,233 0,233" fill="var(--paper)"/>

  <!-- orange arrowhead -->
  <polygon class="arrow-accent" points="287,0 452,140 312,230 285,225 322,140"
           fill="var(--orange)" stroke="var(--white)" stroke-width="5" stroke-linejoin="miter"/>

  <!-- diagonal rules -->
  <line x1="340" y1="0" x2="470" y2="110" stroke="var(--white)" stroke-width="4"/>
  <line x1="640" y1="460" x2="700" y2="546" stroke="var(--white)" stroke-width="3"/>

  <!-- brand name -->
  <rect x="104" y="52" width="52" height="52" fill="var(--teal-navy)"/>
  <text class="wordmark" x="130" y="175" font-size="29" text-anchor="middle" fill="var(--teal-navy)">Harrowfield</text>

  <!-- hexagon photo frame -->
  <polygon points="557,85 754,194 754,412 557,521 360,412 360,194" fill="var(--white)"/>
  <polygon points="557,95 745,199 745,407 557,511 369,407 369,199" fill="var(--orange)"/>
  <polygon points="557,112 730,207 730,399 557,494 384,399 384,207" fill="var(--white)"/>
  <polygon role="img" aria-label="Photo: pipeline worker in hard hat and overalls at yellow railings by blue industrial tanks"
           points="557,116 726,209 726,397 557,490 388,397 388,209" fill="url(#photoTone)"/>

  <!-- headline -->
  <text class="headline-light" x="36" y="336" font-size="40">Manage with</text>
  <text class="headline-bold" x="36" y="390" font-size="38">HARROWFIELD</text>

  <!-- tagline -->
  <polyline points="38,422 46,430 38,438" fill="none" stroke="var(--orange)" stroke-width="5"/>
  <text class="tagline" x="56" y="436" font-size="16">Focused. Collaborative. Safe.</text>
  <polyline points="320,422 312,430 320,438" fill="none" stroke="var(--orange)" stroke-width="5"/>

  <!-- footer band -->
  <polygon class="footer-band" points="0,483 365,483 425,546 0,546" fill="var(--orange)"/>
  <line x1="380" y1="483" x2="440" y2="546" stroke="var(--white)" stroke-width="4"/>
  <text class="url" x="36" y="520" font-size="12">www.harrowfieldcorp.com</text>
</svg>

<!-- Page 2: who we are / what we offer -->
<svg class="page page-services" viewBox="0 0 772 546" xmlns="http://www.w3.org/2000/svg">
  <rect width="772" height="546" fill="var(--night-navy)"/>

  <!-- brand name -->
  <text class="wordmark" x="28" y="104" font-size="18" fill="var(--white)">Harrowfield</text>

  <!-- header bar -->
  <polyline points="190,52 180,63 190,74" fill="none" stroke="var(--orange)" stroke-width="5"/>
  <polygon points="205,52 772,52 772,74 196,74 196,63" fill="var(--white)"/>

  <!-- section heading -->
  <text class="section-head" x="30" y="142" font-size="17.5">
    <tspan fill="var(--white)">WHO WE ARE / </tspan><tspan fill="var(--orange)">WHAT WE OFFER</tspan>
  </text>

  <!-- service 1 -->
  <g class="service">
    <rect x="30" y="158" width="696" height="97" fill="none" stroke="var(--orange)" stroke-width="2.5"/>
    <circle role="img" aria-label="Icon: worker with hard hat and valve" cx="90" cy="206" r="33" fill="var(--white)"/>
    <text class="service-title" x="147" y="180">PIPELINE ABANDONMENT &amp; DECOMMISSIONING</text>
    <g class="service-list">
      <text class="service-item" x="161" y="202">Pipeline pigging and purging services</text>
      <text class="service-item" x="161" y="214">Pipeline branch termination and dead leg elimination</text>
      <text class="service-item" x="161" y="226">Pipeline abandonments</text>
      <text class="service-item" x="161" y="238">Purging and disposal of surface and subsurface production equipment</text>
    </g>
    <g fill="none" stroke="var(--orange)" stroke-width="1.6">
      <polyline points="149,195 153,199 149,203"/><polyline points="149,207 153,211 149,215"/>
      <polyline points="149,219 153,223 149,227"/><polyline points="149,231 153,235 149,239"/>
    </g>
  </g>

  <!-- service 2 -->
  <g class="service">
    <rect x="30" y="273" width="696" height="97" fill="none" stroke="var(--orange)" stroke-width="2.5"/>
    <circle role="img" aria-label="Icon: pipe valve wheel held by hands" cx="90" cy="321" r="33" fill="var(--white)"/>
    <text class="service-title" x="147" y="292">PIPELINE INTEGRITY</text>
    <g class="service-list">
      <text class="service-item" x="161" y="310">Services include operation, inspection, maintenance, HSE and corporate communications</text>
      <text class="service-item" x="161" y="322">Integrity excavation services including locating, excavating, hand exposing, coating removal and sandblasting</text>
      <text class="service-item" x="161" y="334">Coating application</text>
      <text class="service-item" x="161" y="346">Repair and replacement services, cut-out sleeve installation, sleeve repairs and pipeline lowering</text>
    </g>
    <g fill="none" stroke="var(--orange)" stroke-width="1.6">
      <polyline points="149,303 153,307 149,311"/><polyline points="149,315 153,319 149,323"/>
      <polyline points="149,327 153,331 149,335"/><polyline points="149,339 153,343 149,347"/>
    </g>
  </g>

  <!-- service 3 -->
  <g class="service">
    <rect x="30" y="387" width="696" height="98" fill="none" stroke="var(--orange)" stroke-width="2.5"/>
    <circle role="img" aria-label="Icon: oil derrick and fuel pump" cx="90" cy="436" r="33" fill="var(--white)"/>
    <text class="service-title" x="147" y="405">FULL-SCALE PROJECT MANAGEMENT</text>
    <g class="service-list">
      <text class="service-item" x="161" y="420">Pre-job scouting and estimates</text>
      <text class="service-item" x="161" y="432">Access planning, logistics and construction</text>
      <text class="service-item" x="161" y="444">Full scale coordination and collaborative abandonment program management across internal and external stakeholders</text>
      <text class="service-item" x="161" y="456">Construction supervision and monitoring</text>
      <text class="service-item" x="161" y="468">Surface and subsurface information gathering</text>
      <text class="service-item" x="161" y="480">Land packages</text>
    </g>
    <g fill="none" stroke="var(--orange)" stroke-width="1.6">
      <polyline points="149,413 153,417 149,421"/><polyline points="149,425 153,429 149,433"/>
      <polyline points="149,437 153,441 149,445"/><polyline points="149,449 153,453 149,457"/>
      <polyline points="149,461 153,465 149,469"/><polyline points="149,473 153,477 149,481"/>
    </g>
  </g>

  <!-- footer -->
  <polygon points="0,512 150,512 184,546 0,546" fill="var(--orange)"/>
  <text class="url" x="20" y="533" font-size="6.5" letter-spacing="1.5">www.harrowfieldcorp.com</text>

  <g class="footer-tagline">
    <polyline points="540,516 546,523 540,530" fill="none" stroke="var(--orange)" stroke-width="3.5"/>
    <text class="tagline" x="724" y="527" font-size="10.5" text-anchor="end">Focused. Collaborative. Safe.</text>
    <polyline points="740,516 734,523 740,530" fill="none" stroke="var(--orange)" stroke-width="3.5"/>
  </g>
</svg>

</body>
</html>
```